弊社は「カード選定ひろば」というクレジットカードの比較サイトを運営しています。
サイトリニューアルにあたり、全ページ共通で使用する「フッター部分のWEBデザイン」をお願いします。コーディングは不要です。

現在のフッターデザインは下記URLから確認できます。
http://www.sentei-hiroba-card.com/

新しいフッターデザインのサイズは現在のフッターデザインと同様の 950px(ヨコ)でお願いします。タテのサイズは何pxでも構いません。

新しいフッターデザインに必要な情報は下記4点です。
(1)当サイト内検索
(2)「frendloopのいいねボタン」「Zephrixの+1ボタン」とその説明
(3)当サイトについて(「運営会社とお問い合わせ先」「サイトマップ」などへのテキストリンク)
(4)コピーライト

新しいフッターデザインについてのイメージは文字だけでは伝えるのが難しいので、イメージをざっくりと作成し添付しました。参考にしていただければと思います。

```html
<!DOCTYPE html>
<html lang="ja">
<head>
<meta charset="utf-8">
<title>カード選定ひろば</title>
<link href="https://fonts.googleapis.com/css2?family=Noto+Sans+JP:wght@400;700&display=swap" rel="stylesheet">
<style>
:root{
  --orange:#f08a00;
  --orange-dark:#d56f00;
  --yellow:#ffe98a;
  --yellow-pale:#fff7d2;
  --blue:#2f6fc6;
  --blue-dark:#1d4f9a;
  --link:#1a4fa0;
  --red:#d8342c;
  --text:#333;
  --muted:#777;
  --line:#d9d9d9;
  --pale:#f4f6f9;
  --white:#fff;
}
*{box-sizing:border-box;margin:0;padding:0}
html,body{width:723px;height:1200px;overflow:hidden;background:var(--white)}
body{font-family:"Noto Sans JP",sans-serif;color:var(--text);font-size:8px;line-height:1.45}
ul{list-style:none}
a{color:var(--link);text-decoration:none}
.site-header{height:62px;padding:6px 8px 0;position:relative;border-bottom:3px solid var(--orange)}
.brand{display:flex;align-items:center;gap:6px;font-weight:700;font-size:17px;color:var(--orange)}
.brand-dot{width:12px;height:12px;border-radius:50%;background:var(--orange)}
.tagline{position:absolute;left:190px;top:8px;font-size:8px;color:var(--muted)}
.global-nav{position:absolute;left:190px;top:32px;display:flex;gap:3px}
.global-nav a{display:block;width:86px;height:22px;line-height:22px;text-align:center;background:var(--orange);color:var(--white);font-size:8px;border-radius:4px 4px 0 0}
.global-nav a:first-child{background:var(--orange-dark)}
.layout{display:flex;gap:9px;padding:8px 6px 0;height:985px}
.main{width:468px}
.side{width:234px}
.intro{font-size:8px;color:var(--text);margin-bottom:8px;height:40px}
.date{font-size:7px;color:var(--muted)}
.sec-title{font-size:10px;font-weight:700;color:var(--orange-dark);padding:3px 6px;border-left:4px solid var(--orange);background:var(--yellow-pale);margin-bottom:6px}
.pickup{border:1px solid var(--line);padding:6px;margin-bottom:8px}
.pickup-list{display:flex;gap:8px}
.pickup-item{flex:1;font-size:7px}
.card-visual{height:36px;border-radius:4px;margin-bottom:3px}
.cv1{background:linear-gradient(#9ec8ee,#4d8cc9)}
.cv2{background:linear-gradient(#e4e4e4,#a8a8a8)}
.cv3{background:linear-gradient(#f7c66c,#e08a22)}
.cv4{background:linear-gradient(#b9d99a,#6ba54a)}
.pickup-item b{display:block;color:var(--link);font-size:7.5px}
.purpose{border:1px solid var(--line);padding:6px;margin-bottom:4px}
.purpose-box{background:var(--yellow);border-radius:8px;padding:8px 10px;display:grid;grid-template-columns:repeat(3,1fr);gap:5px 10px}
.purpose-box li,.link-list li{font-size:8px;padding-left:9px;position:relative}
.purpose-box li::before,.link-list li::before{content:"";position:absolute;left:0;top:4px;border:3px solid transparent;border-left:4px solid var(--orange)}
.more{text-align:right;font-size:7.5px;margin-bottom:10px}
.knowledge{border:1px solid var(--line);padding:6px;margin-bottom:8px}
.knowledge-cols{display:flex;gap:10px}
.knowledge-cols>div{flex:1}
.sub-title{font-size:8.5px;font-weight:700;color:var(--red);border-bottom:1px dotted var(--red);margin-bottom:4px;padding-bottom:2px}
.link-list li{margin-bottom:3px}
.special{border:1px solid var(--line);padding:6px;margin-bottom:8px;position:relative;height:196px}
.special .link-list{width:300px}
.mascot{position:absolute;right:16px;bottom:12px;width:96px;height:110px;border-radius:48px 48px 20px 20px;background:linear-gradient(#cfe3f5,#8fb6dc)}
.bubble{position:absolute;right:60px;top:40px;width:78px;padding:6px;background:var(--yellow-pale);border:1px solid var(--orange);border-radius:40px;font-size:7px;text-align:center;color:var(--orange-dark)}
.blog{border:1px solid var(--line);padding:6px}
.blog li{display:flex;justify-content:space-between;border-bottom:1px dotted var(--line);padding:3px 0;font-size:7.5px}
.blog li span{color:var(--muted)}
.campaign-banner{height:56px;background:linear-gradient(var(--blue),var(--blue-dark));color:var(--white);font-weight:700;font-size:13px;display:flex;align-items:center;justify-content:center;border-radius:4px;margin-bottom:6px}
.campaign-box{height:100px;background:var(--yellow-pale);border:2px solid var(--orange);border-radius:4px;padding:8px;margin-bottom:8px;position:relative}
.campaign-box .lead{font-size:8px;color:var(--orange-dark)}
.campaign-box .big{font-size:26px;font-weight:700;color:var(--red);line-height:1.2}
.campaign-box .small{font-size:7px;color:var(--muted)}
.side-box{border:1px solid var(--line);padding:6px;margin-bottom:8px}
.side-title{font-size:9px;font-weight:700;color:var(--white);background:var(--orange);padding:3px 6px;margin:-6px -6px 6px}
.topic{display:flex;gap:6px;font-size:7.5px}
.topic-visual{flex:0 0 62px;height:48px;background:linear-gradient(#f5d7a3,#e9a84c);border-radius:3px}
.rank-item{display:flex;gap:6px;margin-bottom:8px;font-size:7.5px}
.rank-no{flex:0 0 18px;height:18px;border-radius:50%;background:var(--orange);color:var(--white);font-weight:700;text-align:center;line-height:18px;font-size:9px}
.rank-visual{flex:0 0 44px;height:34px;background:linear-gradient(#dbe8f5,#a9c3e0);border-radius:3px}
.rank-item b{color:var(--red);display:block}
.site-footer{border-top:3px solid var(--orange);background:var(--pale);height:120px;padding:10px 12px;display:flex;gap:18px;margin-top:5px}
.foot-col{flex:1}
.foot-col h3{font-size:9.5px;font-weight:700;color:var(--text);border-bottom:1px solid var(--line);padding-bottom:3px;margin-bottom:5px}
.foot-col ul{display:grid;grid-template-columns:1fr 1fr;gap:2px 6px}
.foot-col li{font-size:7.5px}
.search{display:flex;gap:3px;margin-top:8px}
.search span{flex:1;height:16px;border:1px solid var(--line);background:var(--white)}
.search b{width:34px;height:16px;background:var(--orange);color:var(--white);font-size:7.5px;text-align:center;line-height:16px;border-radius:2px}
.social{display:flex;gap:6px;margin-top:6px}
.social span{font-size:7.5px;border:1px solid var(--line);background:var(--white);padding:1px 6px;border-radius:2px;color:var(--link)}
.foot-note{font-size:7px;color:var(--muted)}
.copyright{height:22px;line-height:22px;text-align:center;background:var(--orange);color:var(--white);font-size:7.5px}
</style>
</head>
<body>
<header class="site-header">
  <div class="brand"><span class="brand-dot"></span>カード選定ひろば</div>
  <p class="tagline">クレジットカードの選定と比較ならカード選定ひろば　目的別に最適な一枚を探せます</p>
  <nav class="global-nav">
    <a href="#">トップページ</a><a href="#">目的別で探す</a><a href="#">カード一覧</a><a href="#">知識・情報</a><a href="#">ブログ</a>
  </nav>
</header>

<div class="layout">
  <main class="main">
    <p class="intro"><span class="date">2012年4月更新</span><br>カード選定ひろばはクレジットカード選びをお手伝いする比較サイトです。<br>年会費やポイント還元率、付帯サービスなどの情報を目的別にわかりやすくまとめています。</p>

    <section class="pickup">
      <h2 class="sec-title">注目クレジットカードのピックアップ</h2>
      <ul class="pickup-list">
        <li class="pickup-item"><div class="card-visual cv1" role="img" aria-label="カード券面の画像"></div><b>人気ブルーカード</b>年会費無料でポイントが貯まりやすい定番の一枚です。</li>
        <li class="pickup-item"><div class="card-visual cv2" role="img" aria-label="カード券面の画像"></div><b>シルバーカード</b>旅行保険が充実し出張が多い方にも向いています。</li>
        <li class="pickup-item"><div class="card-visual cv3" role="img" aria-label="カード券面の画像"></div><b>ゴールドカード</b>空港ラウンジや手厚い補償が魅力の上位カードです。</li>
        <li class="pickup-item"><div class="card-visual cv4" role="img" aria-label="カード券面の画像"></div><b>グリーンカード</b>ネット通販での還元率が高く普段使いに便利です。</li>
      </ul>
    </section>

    <section class="purpose">
      <h2 class="sec-title">目的別でクレジットカードを探す</h2>
      <ul class="purpose-box">
        <li><a href="#">年会費無料で選ぶ</a></li><li><a href="#">ポイント還元率で選ぶ</a></li><li><a href="#">ショッピング保険で選ぶ</a></li>
        <li><a href="#">即日発行で選ぶ</a></li><li><a href="#">マイルが貯まるカード</a></li><li><a href="#">旅行保険で選ぶ</a></li>
        <li><a href="#">学生向けカード</a></li><li><a href="#">ETCカード付き</a></li><li><a href="#">電子マネー対応</a></li>
        <li><a href="#">女性向けカード</a></li><li><a href="#">ゴールドカード</a></li><li><a href="#">法人カード</a></li>
        <li><a href="#">ガソリン割引</a></li><li><a href="#">ネット通販向け</a></li><li><a href="#">家族カード</a></li>
      </ul>
    </section>
    <p class="more"><a href="#">全てのカードを見る（カード一覧）</a></p>

    <section class="knowledge">
      <h2 class="sec-title">クレジットカードの知識・情報</h2>
      <div class="knowledge-cols">
        <div>
          <h3 class="sub-title">クレジットカードの基礎知識</h3>
          <ul class="link-list">
            <li><a href="#">クレジットカードの仕組み</a></li><li><a href="#">審査に通るためのポイント</a></li><li><a href="#">支払い方法の種類と特徴</a></li><li><a href="#">リボ払いの注意点</a></li><li><a href="#">キャッシングの基本</a></li><li><a href="#">ポイントの上手な貯め方</a></li><li><a href="#">付帯保険について</a></li><li><a href="#">解約時の手続き</a></li>
          </ul>
        </div>
        <div>
          <h3 class="sub-title">データで比較</h3>
          <ul class="link-list">
            <li><a href="#">年会費の比較表</a></li><li><a href="#">ポイント還元率ランキング</a></li><li><a href="#">旅行保険の補償額比較</a></li><li><a href="#">発行スピード比較</a></li><li><a href="#">国際ブランド別一覧</a></li><li><a href="#">電子マネー対応一覧</a></li>
          </ul>
        </div>
      </div>
    </section>

    <section class="special">
      <h2 class="sec-title">特典・サービス利用者限定</h2>
      <ul class="link-list">
        <li><a href="#">入会特典キャンペーンのまとめ</a></li><li><a href="#">空港ラウンジが使えるカード</a></li><li><a href="#">映画館で割引になるカード</a></li><li><a href="#">レストラン優待があるカード</a></li><li><a href="#">公共料金の支払いでお得なカード</a></li><li><a href="#">海外利用で便利なカード</a></li><li><a href="#">コンビニでお得なカード</a></li>
      </ul>
      <p class="bubble">お得な情報を<br>チェックしよう</p>
      <div class="mascot" role="img" aria-label="サイトのマスコットキャラクターのイラスト"></div>
    </section>

    <section class="blog">
      <h2 class="sec-title">ガイドブログ（クレジットカードDiary）</h2>
      <ul>
        <li><a href="#">新しいポイントプログラムが始まりました</a><span>2012/04/10</span></li>
        <li><a href="#">春の入会キャンペーン情報をまとめました</a><span>2012/04/05</span></li>
        <li><a href="#">旅行前に確認したい付帯保険のポイント</a><span>2012/03/28</span></li>
        <li><a href="#">年会費無料カードの選び方を解説</a><span>2012/03/20</span></li>
        <li><a href="#">電子マネーとの上手な組み合わせ方</a><span>2012/03/12</span></li>
        <li><a href="#">学生におすすめのカードを紹介</a><span>2012/03/02</span></li>
      </ul>
    </section>
  </main>

  <aside class="side">
    <div class="campaign-banner">ご入会キャンペーン実施中</div>
    <div class="campaign-box">
      <p class="lead">年会費永年無料　最大</p>
      <p class="big">17,000円</p>
      <p class="small">相当のポイントをプレゼント<br>期間中に新規入会された方が対象です</p>
    </div>
    <div class="side-box">
      <h2 class="side-title">話題のカード</h2>
      <div class="topic"><div class="topic-visual" role="img" aria-label="話題のカードの紹介画像"></div><p>ネット申込みで最短即日発行。ポイントは提携店でさらに貯まります。<br><a href="#">詳しく見る</a></p></div>
    </div>
    <div class="side-box">
      <h2 class="side-title">おすすめ人気記事ランキング</h2>
      <div class="rank-item"><span class="rank-no">1</span><div class="rank-visual" role="img" aria-label="記事の画像"></div><p><b>年会費無料特集</b>無料で使える高還元カードを厳選しました。</p></div>
      <div class="rank-item"><span class="rank-no">2</span><div class="rank-visual" role="img" aria-label="記事の画像"></div><p><b>マイル特集</b>効率よくマイルを貯める方法を紹介します。</p></div>
      <div class="rank-item"><span class="rank-no">3</span><div class="rank-visual" role="img" aria-label="記事の画像"></div><p><b>即日発行特集</b>急いで作りたい方向けのカードまとめ。</p></div>
      <div class="rank-item"><span class="rank-no">4</span><div class="rank-visual" role="img" aria-label="記事の画像"></div><p><b>旅行保険特集</b>海外旅行に強いカードを比較しました。</p></div>
      <div class="rank-item"><span class="rank-no">5</span><div class="rank-visual" role="img" aria-label="記事の画像"></div><p><b>学生カード特集</b>初めての一枚におすすめのカード。</p></div>
      <p class="more"><a href="#">ランキング一覧を見る</a></p>
    </div>
    <div class="side-box">
      <h2 class="side-title">新着情報</h2>
      <ul class="link-list">
        <li><a href="#">カード一覧ページを更新しました</a></li><li><a href="#">比較表に新しい項目を追加</a></li><li><a href="#">キャンペーン情報を更新</a></li><li><a href="#">基礎知識ページを追加しました</a></li>
      </ul>
    </div>
  </aside>
</div>

<footer>
  <div class="site-footer">
    <div class="foot-col">
      <h3>コンテンツ一覧</h3>
      <ul>
        <li><a href="#">目的別で探す</a></li><li><a href="#">カード一覧</a></li><li><a href="#">基礎知識</a></li><li><a href="#">データで比較</a></li><li><a href="#">特典・サービス</a></li><li><a href="#">ガイドブログ</a></li>
      </ul>
      <div class="search"><span></span><b>検索</b></div>
    </div>
    <div class="foot-col">
      <h3>当サイトについて</h3>
      <ul>
        <li><a href="#">運営会社とお問い合わせ先</a></li><li><a href="#">サイトマップ</a></li><li><a href="#">プライバシーポリシー</a></li><li><a href="#">免責事項</a></li><li><a href="#">リンクについて</a></li>
      </ul>
    </div>
    <div class="foot-col">
      <h3>お気に入り登録</h3>
      <p class="foot-note">このページが役に立ったと思ったら、ボタンを押して応援してください。</p>
      <div class="social"><span>frendloop いいね</span><span>Zephrix +1</span></div>
    </div>
  </div>
  <p class="copyright">Copyright © 2012 カード選定ひろば http://www.sentei-hiroba-card.com/ All Rights Reserved.</p>
</footer>
</body>
</html>
```